Create a dynamic design for a photographers site

We need a design for a wordpress web site for a photography business specializing in Hotels, Resorts and Travel Destinations. We have a lot of experience in the US and Caribbean and offer the full service to the client from planning, to production and delivery of the final product.
We are looking for a clean, sharp, modern design with big visuals, options for video. We already have a logo which is blue and black.

With your designs, I'd like to see a second page as well as a front page. I would like it to have a content area and a side bar. Thanks You

Doran

Target Market(s)

Hotels and Marketing people. I'm selling commercial photography mainly to the travel industry with hotels, resorts and destination experiences. I also shoot for retail stores, restaurants. Also do lifestyle with models that fits into any of the above.

Industry/Entity Type

Business

Colors

Designer to choose colors to be used in the design.

Requirements
Must have
• Big visuals.
Opportunity to showcase video,
Social Media links,
Blog

```html
<!DOCTYPE html>
<html lang="en">
<head>
<meta charset="utf-8">
<title>Lakeside Lens – Travel &amp; Resort Photography</title>
<link href="https://fonts.googleapis.com/css2?family=Source+Sans+3:ital,wght@0,400;0,600;0,700;1,400;1,700&display=swap" rel="stylesheet">
<style>
:root{
  --blue:#0a8ed3;
  --blue-dark:#0b79b5;
  --ink:#222;
  --body:#444;
  --line:#e2e2e2;
  --panel:#efefef;
  --footer-dark:#231f20;
  --white:#fff;
}
*{margin:0;padding:0;box-sizing:border-box}
html,body{width:762px;height:1200px;overflow:hidden;background:var(--white)}
body{position:relative;font-family:"Source Sans 3",Arial,sans-serif;color:var(--body)}
.abs{position:absolute}
.brand{left:121px;top:14px;font-size:19px;font-weight:700;color:var(--blue);display:flex;align-items:center;gap:6px}
.brand .dot{width:12px;height:12px;background:var(--ink);border-radius:50%}
.search{left:505px;top:17px;width:136px;height:18px;background:#ececec}
.search svg{position:absolute;right:6px;top:3px}
.nav{left:0;top:50px;width:762px;height:27px;background:var(--blue);display:flex;align-items:center;padding-left:128px}
.nav a{color:var(--white);font-size:7px;font-weight:600;text-decoration:none;margin-right:20px}
.hero{left:0;top:77px;width:762px;height:290px;background:linear-gradient(180deg,#5fa9e0 0%,#9cc9ea 28%,#b89a6a 42%,#7d6a4d 58%,#28c3c0 72%,#1fb7b8 100%)}
.quote{left:0;top:266px;width:762px;text-align:center;color:var(--white);font-weight:700;font-size:15px;line-height:22px;text-transform:uppercase;text-shadow:0 1px 3px rgba(0,0,0,.45)}
.quote small{display:block;font-size:10.5px;margin-top:4px}
.dots{left:360px;top:342px;display:flex;gap:12px;align-items:center}
.dots i{width:3px;height:3px;border-radius:50%;background:var(--white);display:block}
.dots i.on{width:11px;height:11px;border:1.5px solid #123;background:transparent}

.main-col{left:122px;top:395px;width:315px}
h2.sec{font-size:11.5px;font-weight:400;color:var(--ink);line-height:14px}
.txt{font-size:5.8px;line-height:10.2px;text-align:justify}
.photo{float:left;width:152px;height:72px;margin:0 10px 4px 0;border:1px solid #ccc;background:linear-gradient(180deg,#7fb8e0 0%,#5aaad0 45%,#e8dcc0 70%,#d9c9a6 100%)}
.who-intro{margin-top:7px}
.who-intro::after{content:"";display:block;clear:both}
.who-split{display:flex;gap:10px;margin-top:0}
.who-split .txt{width:200px;text-align:left}
.pull{flex:1;font-style:italic;font-size:5.8px;line-height:10.2px;border-left:1px solid #ccc;padding-left:10px;margin-top:6px;align-self:flex-start}
.gap{margin-top:8px}
.rule{height:1px;background:var(--line)}
.icons{display:flex;gap:11px;margin-top:8px}
.icons span{width:30px;height:30px;border:1px solid #bbb;display:flex;align-items:center;justify-content:center}
.icons b{width:12px;height:12px;background:var(--blue);border-radius:50%}
.cols{display:flex;margin-top:14px}
.cols .lead{width:95px;font-size:6.4px;line-height:10.2px;padding-right:6px}
.cols .divider{width:1px;background:#ccc;margin:0 10px 0 6px}
.cols .txt{flex:1}

h3.side{font-size:8px;font-weight:600;color:var(--ink);text-transform:uppercase}
.clients{left:487px;top:416px;display:grid;grid-template-columns:71px 71px;gap:10px 10px}
.clients div{height:36px;background:var(--panel);box-shadow:0 2px 3px rgba(0,0,0,.18);display:flex;align-items:center;justify-content:center;font-size:7px;font-weight:600;color:#555}
.card{background:var(--panel);box-shadow:0 3px 4px rgba(0,0,0,.2);padding:8px 10px}
.card .who{font-size:6.5px;font-weight:700;font-style:italic;color:var(--ink)}
.arrows{position:absolute;right:10px;top:8px;display:flex;gap:4px}
.arrows i{width:10px;height:10px;background:var(--blue-dark);display:block;color:#fff;font-style:normal;font-size:7px;line-height:10px;text-align:center}
.card p{font-size:5.6px;line-height:10px;margin-top:4px}
.avatar{width:31px;height:30px;flex:none;background:linear-gradient(180deg,#7fc0a0,#3d8a5a 60%,#d6e7ef);border:1px solid #bbb}

.footer{left:0;top:976px;width:762px;height:178px;background:var(--blue);color:var(--white)}
.footer h4{position:absolute;top:36px;font-size:10px;font-weight:400;text-transform:uppercase}
.footer p,.footer li{font-size:6.2px;line-height:10.2px}
.footer ul{list-style:none}
.contact li{display:flex;align-items:center;gap:10px;margin-top:4px}
.tweet{display:flex;gap:8px;margin-bottom:4px}
.tweet i{flex:none;width:7px;height:7px;border-radius:50%;background:var(--white);margin-top:2px}
.news{top:1071px;left:539px;display:flex}
.news span{width:80px;height:18px;background:var(--white);color:#aaa;font-size:6.2px;padding:5px 8px}
.news b{width:22px;height:18px;background:var(--footer-dark);color:#fff;font-size:6.2px;text-align:center;line-height:18px;font-weight:400}
.bottom{left:0;top:1154px;width:762px;height:46px;background:var(--footer-dark);color:var(--white);font-size:6px}
.social{position:absolute;right:152px;top:15px;display:flex;gap:4px}
.social i{width:14px;height:14px;border-radius:50%;background:var(--blue);display:block}
</style>
</head>
<body>
<header>
  <div class="abs brand"><span class="dot"></span>Lakeside Lens</div>
  <div class="abs search"><svg width="12" height="12" viewBox="0 0 12 12"><circle cx="5" cy="5" r="3.6" fill="none" stroke="#0a8ed3" stroke-width="1.6"/><line x1="7.7" y1="7.7" x2="11" y2="11" stroke="#0a8ed3" stroke-width="1.8"/></svg></div>
  <nav class="abs nav">
    <a>Home</a><a>About Us</a><a>Our Services</a><a>Contact Us</a><a>Client List</a><a>Video Work</a><a>Portfolio</a><a>Aerial Photography</a><a>Blog</a><a>Photography</a>
  </nav>
</header>

<section class="abs hero" role="img" aria-label="Photograph of thatched overwater bungalows above a turquoise lagoon under a blue sky"></section>
<div class="abs quote">Which of my photographs is my favourite? The one I'm<br>going to take tomorrow.<small>--Mara Ellison</small></div>
<div class="abs dots"><i></i><i class="on"></i><i></i></div>

<main class="abs main-col">
  <h2 class="sec">Who we are</h2>
  <div class="who-intro">
    <div class="photo" role="img" aria-label="Photograph of a beach table under a white umbrella by a calm bay"></div>
    <p class="txt">Lorem Ipsum telah menjadi text contoh semenjak tahun ke 1500an, apabila pencetak yang kurang terkenal mengambil sebuah galeri cetak dan merobakanya menjadi satu buku spesimen. Ia telah bertahan bukan hanya selama lima kurunsit amet, consectetur adipiscing elit. Lorem Ipsum adalah text contoh digunakan didalam industri pencetakan dan typesetting. Lorem Ipsum telah menjadi text contoh semenjak tahun ke 1500an, apabila pencetak yang kurang Nam magna sem, tristique id facilisis non, ullamcorper vel velit. Sed scelerisque, quam ac pharetra lacinia, lorem rutrum orci, pharetra augue ipsum dolor sit amet, consectetur adipiscing elit. Nam magna sem, tristique id facilisis non, ullamcorper vel velit. Sed scelerisque, quam ac pharetra lacinia, lorem rutrum</p>
  </div>
  <div class="who-split">
    <p class="txt">magna sem, tristique id facilisis non, ullamcorper vel velit. Sed scelerisque, quam ac pharetra lacinia, lorem rutrum orci, pharetra augue ipsum dolor sit amet, consectetur adipiscing elit.<br><br>Nam magna sem, tristique id facilisis non, ullamcorper vel velit. Sed scelerisque, quam ac pharetra lacinia, lorem.</p>
    <p class="pull">Lorem Ipsum yang sedia ada, tetapi kebanyakkannya telah diubahsuai, lawak jenaka diselitkan, atau ayat yang di sertakan .</p>
  </div>
  <p class="txt gap">Ada banyak versi dari mukasurat-mukasurat Lorem Ipsum yang sedia ada, tetapi kebanyakkannya telah diubahsuai, lawak jenaka diselitkan, atau ayat ayat yang di sertakan secara rambang yang lansung tidak munasabah. Jika anda ingin menggunakan Lorem Ipsum, anda perlu memastikan bahwa tiada apa yang memalukan akan terselit didalam di tengah tengah kandungan text. Semua injin Lorem Ipsum didalam Internet hanya mengulangi text, sekaligus menjadikan injin kami sebagai yang terunggul dan tepat sekali di Internet. Ia menggunakan kamus yang mengandungi lebih 200 ayat Latin bersama model dan struktur ayat Latin, untuk menghasilkan Lorem Ipsum yang munasabah. Hasil pengeluaran Lorem Ipsum kami adalah bebas dari ulangan ungkapan-ungkapan, lawak jenaka atau ayat ayat yang tidak bercirikan bahasa latin terselit didalam di.</p>
  <div class="rule" style="margin-top:28px"></div>

  <h2 class="sec" style="margin-top:18px">Why choose us</h2>
  <div class="icons"><span><b></b></span><span><b></b></span><span><b></b></span><span><b></b></span><span><b></b></span><span><b></b></span><span><b></b></span><span><b></b></span></div>
  <p class="txt" style="margin-top:8px">Ada banyak versi dari mukasurat-mukasurat Lorem Ipsum yang sedia ada, tetapi kebanyakkannya telah diubahsuai, lawak jenaka diselitkan, atau ayat ayat yang di sertakan secara rambang yang lansung tidak munasabah. Jika anda ingin menggunakan Lorem Ipsum, anda perlu memastikan bahwa tiada apa yang memalukan akan terselit didalam di tengah tengah kandungan text. Semua injin Lorem Ipsum didalam Internet hanya mengulangi text, sekaligus menjadikan injin kami sebagai yang terunggul dan tepat sekali di Internet. Ia menggunakan kamus yang mengandungi lebih 200 ayat Latin.</p>
  <div class="cols">
    <p class="lead">Neque porro quisquam est qui dolorem ipsum quia dolor sit amet, consectetur, adipisci velit tetapi kebanyakkannya telah diubahsuai...</p>
    <span class="divider"></span>
    <p class="txt">Ada banyak versi dari mukasurat-mukasurat Lorem Ipsum yang sedia ada, tetapi kebanyakkannya telah diubahsuai, lawak jenaka diselitkan, atau ayat ayat yang di sertakan secara rambang yang lansung tidak munasabah. Jika anda ingin menggunakan Lorem Ipsum, anda perlu memastikan bahwa tiada apa yang memalukan akan terselit didalam di tengah tengah kandungan text. Semua injin</p>
  </div>
  <p class="txt" style="margin-top:6px;width:300px;text-align:left">Semua injin Lorem Ipsum didalam Internet hanya mengulangi text, sekaligus menjadikan injin kami sebagai menggunakan kamus yang mengandungi lebih 200 ayat Latin.</p>
</main>

<aside>
  <h3 class="abs side" style="left:486px;top:398px">Our most famous clients</h3>
  <div class="abs clients">
    <div>Emberline</div><div>Clearwell</div><div>Hale &amp; Partners</div><div>Bright Meadow</div>
    <div>Northfold</div><div>Quillstone</div><div>Vowcraft</div><div>Bean Corner</div>
  </div>
  <div class="abs rule" style="left:486px;top:608px;width:154px"></div>

  <h3 class="abs side" style="left:486px;top:627px">Testimonials</h3>
  <div class="abs card" style="left:487px;top:647px;width:152px;height:90px">
    <div class="who">Peter Lowell, USA</div>
    <div class="arrows"><i>‹</i><i>›</i></div>
    <p>Ada banyak versi dari mukasurat Lorem Ipsum yang sedia ada, tetapi kebanyakkannya telah diubahsuai, lawak jenaka diselitkan, atau ayat ayat yang di sertakan secara rambang yang lansung tidak munasabah.<br>Jika anda ingin.</p>
  </div>
  <div class="abs rule" style="left:486px;top:756px;width:154px"></div>

  <h3 class="abs side" style="left:486px;top:774px">Meet the teem</h3>
  <div class="abs card" style="left:487px;top:793px;width:152px;height:117px">
    <div style="display:flex;gap:9px">
      <div class="avatar" role="img" aria-label="Portrait photo of team member outdoors"></div>
      <div><div class="who">CELIA BRANDT</div><p style="margin-top:2px;font-style:italic">29 years old</p><p style="margin-top:0">Resort Expert</p></div>
    </div>
    <div class="arrows"><i>‹</i><i>›</i></div>
    <p>Versi dari mukasurat Lorem Ipsum yang sedia ada, tetapi kebanyakkannya telah diubahsuai, lawak jenaka diselitkan, ayat ayat yang di sertakan secara rambang Lorem Ipsum, anda perlu bahwa tiada apa akan terselit didalam.<br>text. Semua injin Lorem Ipsum didalam Internet</p>
  </div>
</aside>

<footer class="abs footer">
  <h4 style="left:120px">About Doran</h4>
  <p class="abs" style="left:121px;top:59px;width:106px">There are many variations of passages of Lorem Ipsum available, but the majority have suffered alteration in some form, by injected humour, or randomised words which don't look even slightly believable. If you are going to use a passage of Lorem Ipsum, you need</p>

  <h4 style="left:260px">Contact</h4>
  <div class="abs" style="left:258px;top:59px;width:106px">
    <p>There are many variations of passages of Lorem Ipsum available, but the majority have suffered alteration in so</p>
    <ul class="contact">
      <li><svg width="8" height="9" viewBox="0 0 8 9"><path d="M4 0a3 3 0 0 1 3 3c0 2-3 6-3 6S1 5 1 3a3 3 0 0 1 3-3z" fill="#fff"/><circle cx="4" cy="3" r="1" fill="#0a8ed3"/></svg>Adress</li>
      <li><svg width="9" height="7" viewBox="0 0 9 7"><rect width="9" height="7" fill="#fff"/><path d="M0 0l4.5 4L9 0" fill="none" stroke="#0a8ed3"/></svg>info@ lakesidelens.com</li>
      <li><svg width="8" height="8" viewBox="0 0 8 8"><path d="M1 0h2l1 2-1 1c.5 1 1 1.5 2 2l1-1 2 1v2c-4 0-7-3-7-7z" fill="#fff"/></svg>555-0199-2468</li>
    </ul>
  </div>

  <h4 style="left:392px">Latest tweets</h4>
  <div class="abs" style="left:392px;top:59px;width:122px">
    <div class="tweet"><i></i><p>Lorem Ipsum is simply dummy text of the printing and typesetting industry. Lorem Ipsum has been the industry's standard dummy<br>1 Hour Ago</p></div>
    <div class="tweet"><i></i><p>Lorem Ipsum is simply dummy text of the printing and typesetting<br><br>1 Hour Ago</p></div>
  </div>

  <h4 style="left:541px">News letter</h4>
  <p class="abs" style="left:539px;top:59px;width:104px">Type your email address below and recive our daily news letter for free</p>
</footer>
<div class="abs news"><span>Email Address</span><b>GO</b></div>

<div class="abs bottom">
  <p style="position:absolute;left:121px;top:20px">©Copy right 2014 <b>Lakeside Lens Studio</b> | All rights reserved.</p>
  <div class="social"><i aria-label="Social link A"></i><i aria-label="Social link B"></i><i aria-label="Social link C"></i></div>
</div>
</body>
</html>
```